Trading journal (Corvanta Loop)

I need a design for trading journal application.
I would like to start from dark version of the design and the main goal that it should be pretty intuitive for everyone. I am going to create the app from scratch and I don't have any logo or branding colors, so it is up to you to choose a color scheme but it is a dark mode, so one of the colors would be black obviously.
The app will be available for web PC, Android and iOS.

There is google document with the requirements.
https://files.plomivex.net/sheet/7QwZrT2kLpN9vB4xHs0Jd8YcGm3FaUe6/view?mode=open

Target Market(s)

Professional traders

Industry/Entity Type

Trading

Colors

Designer to choose colors to be used in the design.

Requirements
Must have
• Dark mode design for PC and mobile views, the design must be pretty intuitive for everyone.
Nice to have
• Tooltips for something non obvious; popovers after completing some actions

```html
<!DOCTYPE html>
<html lang="en">
<head>
<meta charset="utf-8">
<title>Corvanta Loop – Dashboard</title>
<link href="https://fonts.googleapis.com/css2?family=Poppins:wght@400;500;600;700&display=swap" rel="stylesheet">
<style>
:root{
  --bg:#0e0f10;
  --panel:#17191b;
  --card:#222427;
  --row:#25282b;
  --line:#2c2f33;
  --text:#ffffff;
  --muted:#a7abb0;
  --dim:#6f7479;
  --green:#1fd38a;
  --teal:#19c3b4;
  --blue:#1c9ff0;
  --red:#ef4444;
}
*{box-sizing:border-box;margin:0;padding:0}
html,body{width:1200px;height:810px;overflow:hidden;background:var(--bg);font-family:'Poppins',sans-serif;color:var(--text)}
.app{position:relative;width:1200px;height:810px;background:var(--bg)}
.brand{position:absolute;left:33px;top:26px;display:flex;align-items:center;gap:14px}
.brand-mark{width:34px;height:34px;border-radius:8px;background:linear-gradient(135deg,var(--blue),var(--green))}
.brand-name{font-size:13px;font-weight:500;letter-spacing:.3px}
.greeting{position:absolute;left:252px;top:36px;font-size:12px;color:#e6e6e6}
.account{position:absolute;left:900px;top:21px;width:153px;height:46px;border:1px solid var(--line);border-radius:8px;display:flex;align-items:center;gap:8px;padding:0 12px;font-size:10px;font-weight:500}
.account .chev{margin-left:auto;width:14px;height:14px;border-radius:50%;background:#2b2e31;display:flex;align-items:center;justify-content:center}
.bell{position:absolute;left:1080px;top:34px}
.bell .badge{position:absolute;left:9px;top:-6px;width:13px;height:13px;border-radius:50%;background:var(--green);font-size:7px;font-weight:600;color:#000;display:flex;align-items:center;justify-content:center}
.avatar{position:absolute;left:1130px;top:25px;width:34px;height:34px;border-radius:50%;background:linear-gradient(135deg,#5b7fa6,#a48a6a)}
.nav{position:absolute;left:20px;top:114px;width:167px;list-style:none}
.nav li{height:47px;display:flex;align-items:center;gap:14px;padding-left:14px;font-size:11px;color:#e4e4e4;margin-bottom:7px;border-radius:10px}
.nav li.active{background:#1b1d1f;color:var(--green)}
.copyright{position:absolute;left:20px;top:688px;font-size:10px;line-height:15px;color:var(--dim);width:150px}
.main{position:absolute;left:225px;top:89px;width:941px;height:681px;background:var(--panel);border:1px solid #222528;border-radius:16px}
.page-title{position:absolute;left:27px;top:36px;display:flex;align-items:center;gap:12px}
.page-title h1{font-size:21px;font-weight:600}
.updated{font-size:8.5px;color:#cfd2d5;display:flex;align-items:center;gap:6px}
.import{position:absolute;left:816px;top:31px;width:98px;height:39px;border-radius:20px;background:linear-gradient(90deg,var(--blue),var(--green));display:flex;align-items:center;justify-content:center;gap:8px;font-size:12px;font-weight:600}
.stats{position:absolute;left:27px;top:95px;display:flex;gap:18px}
.stat{position:relative;width:163px;height:120px;border-radius:12px;padding:14px 13px;border:1px solid #2a2d31;background:var(--card)}
.stat .ico{width:34px;height:34px;border-radius:50%;display:flex;align-items:center;justify-content:center;border:2px solid rgba(255,255,255,.25)}
.stat .info{position:absolute;right:12px;top:14px}
.stat .value{margin-top:16px;font-size:18px;font-weight:700}
.stat .label{font-size:8.5px;color:#c9ccd0;margin-top:2px;letter-spacing:.2px}
.s-profit{background:linear-gradient(135deg,#4a2a86 0%,#2a2535 45%,var(--card) 75%)}
.s-profit .ico{background:#7b45e6}
.s-avg{background:linear-gradient(135deg,#17417a 0%,#1f2a38 45%,var(--card) 75%)}
.s-avg .ico{background:#1f6fd8}
.s-trades{background:linear-gradient(135deg,#145a37 0%,#1d2f27 45%,var(--card) 75%)}
.s-trades .ico{background:#1ea862}
.s-win{background:linear-gradient(135deg,#7a3418 0%,#35251f 45%,var(--card) 75%)}
.s-win .ico{background:#f0672d}
.s-fees{background:linear-gradient(135deg,#6e1a26 0%,#33222a 45%,var(--card) 75%)}
.s-fees .ico{background:#d3304a}
.chart-title{position:absolute;left:27px;top:282px;font-size:15px;font-weight:600;display:flex;align-items:center;gap:8px}
.toggle{position:absolute;left:302px;top:275px;width:234px;height:36px;border:1px solid var(--line);border-radius:6px;background:#141618;display:flex;align-items:center;padding:3px}
.toggle span{flex:1;text-align:center;font-size:7.5px;font-weight:500;height:28px;line-height:28px;border-radius:4px}
.toggle .on{background:#22262a;color:var(--green)}
.chart{position:absolute;left:0;top:330px}
.trades-card{position:absolute;left:569px;top:275px;width:345px;height:376px;background:#141618;border:1px solid #23262a;border-radius:14px}
.trades-card h2{position:absolute;left:17px;top:22px;font-size:13.5px;font-weight:500;display:flex;align-items:center;gap:8px}
.thead,.trow{position:absolute;left:17px;width:309px;display:grid;grid-template-columns:84px 58px 58px 54px 1fr;align-items:center;padding:0 12px}
.thead{top:68px;font-size:7px;color:#cfd2d5}
.trow{height:51px;background:var(--row);border-radius:8px;font-size:10px;font-weight:500}
.sym{display:flex;align-items:center;gap:8px;font-weight:600}
.coin{width:22px;height:22px;border-radius:50%;flex:none}
.px{display:flex;align-items:center;gap:5px;font-size:9.5px}
.px i{width:8px;height:8px;border-radius:50%;background:#6b7075;display:inline-block}
.pill{width:44px;height:17px;border-radius:9px;background:#181a1c;font-size:7px;font-weight:500;display:flex;align-items:center;justify-content:center}
.pill.close{color:var(--red)}
.pill.open{color:var(--green)}
.pnl{text-align:right;font-size:10px;font-weight:600;line-height:12px;white-space:nowrap}
.pnl small{display:block;font-size:7px;font-weight:400;color:var(--green)}
.pnl.neg small{color:var(--red)}
.thead .pr{text-align:right}
</style>
</head>
<body>
<div class="app">
  <div class="brand"><div class="brand-mark"></div><div class="brand-name">Corvanta Loop</div></div>
  <div class="greeting">Good day, Marin!</div>
  <div class="account">
    <svg width="18" height="16" viewBox="0 0 18 16" fill="none" stroke="#1c9ff0" stroke-width="1.5"><rect x="1" y="3" width="16" height="12" rx="2"/><path d="M3 3l9-2v2M12 8h5v4h-5z"/></svg>
    IB #J208645...
    <span class="chev"><svg width="7" height="5" viewBox="0 0 7 5"><path d="M1 1l2.5 2.5L6 1" stroke="#1fd38a" fill="none" stroke-width="1.3"/></svg></span>
  </div>
  <div class="bell">
    <svg width="16" height="18" viewBox="0 0 16 18" fill="none" stroke="#cfd2d5" stroke-width="1.4"><path d="M3 13V8a5 5 0 0110 0v5l1.5 1.5h-13z"/><path d="M6.5 16.5h3"/></svg>
    <span class="badge">4</span>
  </div>
  <div class="avatar" role="img" aria-label="User profile photo"></div>

  <ul class="nav">
    <li class="active"><svg width="18" height="18" viewBox="0 0 18 18" fill="none" stroke="#1fd38a" stroke-width="1.5"><rect x="1.5" y="1.5" width="15" height="15" rx="3"/><path d="M7 1.5v15M7 8h9.5"/></svg>Dashboard</li>
    <li><svg width="18" height="18" viewBox="0 0 18 18" fill="none" stroke="#e4e4e4" stroke-width="1.4"><rect x="1.5" y="1.5" width="15" height="15" rx="3"/><path d="M5 13v-3M9 13V8M13 13V5M4 8l4-3 3 2 3-3"/></svg>Trade</li>
    <li><svg width="18" height="18" viewBox="0 0 18 18" fill="none" stroke="#e4e4e4" stroke-width="1.4"><rect x="1.5" y="3" width="15" height="13.5" rx="3"/><path d="M1.5 7h15M6 1v4M12 1v4M6 11h.5M9 11h.5M12 11h.5"/></svg>Calendar</li>
    <li><svg width="18" height="18" viewBox="0 0 18 18" fill="none" stroke="#e4e4e4" stroke-width="1.4"><path d="M9 1l7 4v8l-7 4-7-4V5z"/><circle cx="9" cy="9" r="2.5"/></svg>Settings</li>
    <li><svg width="18" height="18" viewBox="0 0 18 18" fill="none" stroke="#e4e4e4" stroke-width="1.4"><rect x="1.5" y="1.5" width="15" height="15" rx="4"/><circle cx="9" cy="7" r="2.5"/><path d="M4.5 14.5c1-2.5 8-2.5 9 0"/></svg>My Account</li>
  </ul>
  <p class="copyright">Copyright © 2024. Corvanta Loop. All Rights Reserved.</p>

  <section class="main">
    <div class="page-title">
      <h1>Dashboard</h1>
      <span class="updated"><svg width="11" height="11" viewBox="0 0 12 12" fill="none" stroke="#cfd2d5" stroke-width="1.2"><path d="M10.5 6A4.5 4.5 0 116 1.5M6 1.5l1.5-1M6 1.5l1.5 1.2"/></svg>LAST UPDATED: JAN 20, 2024&nbsp; 12:28 PM</span>
    </div>
    <div class="import"><svg width="16" height="16" viewBox="0 0 16 16" fill="none" stroke="#fff" stroke-width="1.5"><path d="M14 8A6 6 0 112.5 4.5M8 8l4-4M2 2.5v2.5h2.5"/></svg>Import</div>

    <div class="stats">
      <div class="stat s-profit"><div class="ico"><svg width="16" height="16" viewBox="0 0 16 16" fill="none" stroke="#fff" stroke-width="1.4"><rect x="1.5" y="1.5" width="13" height="13" rx="4"/><path d="M4.5 10l2.5-2.5 2 2 2.5-3"/></svg></div><svg class="info" width="14" height="14" viewBox="0 0 14 14" fill="none" stroke="#9ea2a7"><circle cx="7" cy="7" r="6.2"/><path d="M7 6v4M7 4v.5"/></svg><div class="value">$1600</div><div class="label">TOTAL NET PROFIT</div></div>
      <div class="stat s-avg"><div class="ico"><svg width="16" height="16" viewBox="0 0 16 16" fill="none" stroke="#fff" stroke-width="1.4"><rect x="1.5" y="1.5" width="13" height="13" rx="4"/><path d="M2 8h3l1.5-2.5 2 4.5L10 8h4"/></svg></div><svg class="info" width="14" height="14" viewBox="0 0 14 14" fill="none" stroke="#9ea2a7"><circle cx="7" cy="7" r="6.2"/><path d="M7 6v4M7 4v.5"/></svg><div class="value">50%</div><div class="label">AVERAGE WIN/LOSS</div></div>
      <div class="stat s-trades"><div class="ico"><svg width="16" height="16" viewBox="0 0 16 16" fill="none" stroke="#fff" stroke-width="1.4"><path d="M1.5 14.5h13"/><rect x="3" y="7" width="2.5" height="6" rx="1"/><rect x="7" y="4" width="2.5" height="9" rx="1"/><rect x="11" y="2" width="2.5" height="11" rx="1"/></svg></div><svg class="info" width="14" height="14" viewBox="0 0 14 14" fill="none" stroke="#9ea2a7"><circle cx="7" cy="7" r="6.2"/><path d="M7 6v4M7 4v.5"/></svg><div class="value">304</div><div class="label">TOTAL # OF TRADES</div></div>
      <div class="stat s-win"><div class="ico"><svg width="16" height="16" viewBox="0 0 16 16" fill="none" stroke="#fff" stroke-width="1.4"><path d="M14 8A6 6 0 112 8a6 6 0 016-6"/><path d="M10 6.2c-.5-1-3.5-1.2-3.5.6s3.5.9 3.5 2.7-3 1.6-3.5.6M8 4v1M8 11v1M11 2.5l2.5 0v2.5"/></svg></div><svg class="info" width="14" height="14" viewBox="0 0 14 14" fill="none" stroke="#9ea2a7"><circle cx="7" cy="7" r="6.2"/><path d="M7 6v4M7 4v.5"/></svg><div class="value">50%</div><div class="label">WIN RATE</div></div>
      <div class="stat s-fees"><div class="ico"><svg width="16" height="16" viewBox="0 0 16 16" fill="none" stroke="#fff" stroke-width="1.4"><circle cx="6.5" cy="6.5" r="5"/><circle cx="11" cy="11" r="3.5"/><path d="M8 5c-.3-.7-2.8-.8-2.8.5s2.8.7 2.8 2-2.5 1.1-2.8.4"/></svg></div><svg class="info" width="14" height="14" viewBox="0 0 14 14" fill="none" stroke="#9ea2a7"><circle cx="7" cy="7" r="6.2"/><path d="M7 6v4M7 4v.5"/></svg><div class="value">$1,097</div><div class="label">FEES &amp; COMMISSION</div></div>
    </div>

    <div class="chart-title">Daily Net&nbsp;Cumulative P&amp;L <svg width="14" height="14" viewBox="0 0 14 14" fill="none" stroke="#9ea2a7"><circle cx="7" cy="7" r="6.2"/><path d="M7 6v4M7 4v.5"/></svg></div>
    <div class="toggle"><span>DAILY</span><span class="on">WEEKLY</span><span>MONTHLY</span></div>

    <svg class="chart" width="560" height="290" viewBox="0 0 560 290" font-family="Poppins, sans-serif">
      <defs>
        <linearGradient id="area" x1="0" y1="0" x2="1" y2="1">
          <stop offset="0" stop-color="#1a7f73"/>
          <stop offset=".6" stop-color="#1b5a60"/>
          <stop offset="1" stop-color="#1fd38a"/>
        </linearGradient>
        <linearGradient id="fade" x1="0" y1="0" x2="0" y2="1">
          <stop offset="0" stop-color="#17191b" stop-opacity="0"/>
          <stop offset="1" stop-color="#1b2430" stop-opacity=".9"/>
        </linearGradient>
      </defs>
      <g font-size="10" fill="#cfd2d5" text-anchor="end">
        <text x="55" y="16">$6,000</text><text x="55" y="48">$5,000</text><text x="55" y="80">$4,000</text>
        <text x="55" y="112">$3,000</text><text x="55" y="144">$2,000</text><text x="55" y="176">$1,000</text>
        <text x="55" y="208">$0</text><text x="55" y="240">$-1,000</text>
      </g>
      <g stroke="#2f3236" stroke-dasharray="2 2">
        <path d="M88 13H535M88 45H535M88 76H535M88 108H535M88 140H535M88 172H535M88 203H535M88 235H535"/>
      </g>
      <path d="M88 187C100 182 112 177 125 171.5C155 155 180 138 203 140C240 142 270 213 308 213C345 213 365 140 400 124C430 108 460 88 493 82C510 78 525 72 535 71L535 235L88 235Z" fill="url(#area)"/>
      <path d="M88 140H535V235H88Z" fill="url(#fade)"/>
      <path d="M88 187C100 182 112 177 125 171.5C155 155 180 138 203 140C240 142 270 213 308 213C345 213 365 140 400 124C430 108 460 88 493 82C510 78 525 72 535 71" fill="none" stroke="#fff" stroke-width="1.5"/>
      <g fill="#17191b" stroke="#fff" stroke-width="2.5">
        <circle cx="125" cy="171.5" r="6"/><circle cx="203" cy="140" r="6"/><circle cx="308" cy="213" r="6"/><circle cx="400" cy="124" r="6"/><circle cx="493" cy="82" r="6"/>
      </g>
      <g font-size="8" font-weight="600" fill="#fff" text-anchor="middle">
        <rect x="103" y="140" width="44" height="16" rx="8" fill="#111214"/><text x="125" y="151">$1,000</text>
        <rect x="181" y="108" width="44" height="16" rx="8" fill="#111214"/><text x="203" y="119">$2,000</text>
        <rect x="286" y="182" width="44" height="16" rx="8" fill="#111214"/><text x="308" y="193">-$300</text>
        <rect x="471" y="51" width="44" height="16" rx="8" fill="#111214"/><text x="493" y="62">$3,830</text>
        <rect x="353" y="66" width="84" height="30" rx="15" fill="#111214"/>
        <circle cx="370" cy="81" r="8" fill="#1fd38a"/>
        <path d="M370 85.5v-8M366.5 80.5l3.5-3.5 3.5 3.5" stroke="#111214" stroke-width="1.6" fill="none"/>
        <text x="384" y="80" font-size="10" text-anchor="start">$2,500</text>
        <text x="384" y="90" font-size="6.5" font-weight="400" fill="#bfc3c7" text-anchor="start">JAN 14-20</text>
      </g>
      <g font-size="8.5" fill="#cfd2d5" text-anchor="middle">
        <text x="125" y="268">WEEK 1</text><text x="216" y="268">WEEK 2</text><text x="308" y="268">WEEK 3</text><text x="400" y="268">WEEK 4</text><text x="493" y="268">WEEK 5</text>
      </g>
    </svg>

    <div class="trades-card">
      <h2>Opened and Recent Trades <svg width="14" height="14" viewBox="0 0 14 14" fill="none" stroke="#9ea2a7"><circle cx="7" cy="7" r="6.2"/><path d="M7 6v4M7 4v.5"/></svg></h2>
      <div class="thead"><span>SYMBOL</span><span>ENTRY PRICE</span><span>EXIT PRICE</span><span>STATUS</span><span class="pr">PROFIT</span></div>
      <div class="trow" style="top:91px"><span class="sym"><i class="coin" style="background:#f7931a"></i>KRV</span><span class="px"><i></i>1.271</span><span class="px"><i></i>1.378</span><span class="pill close">CLOSE</span><span class="pnl">+$320<small>+1.8%</small></span></div>
      <div class="trow" style="top:146px"><span class="sym"><i class="coin" style="background:#58bf00"></i>ZEL</span><span class="px"><i></i>1.308</span><span class="px"><i></i>1.22</span><span class="pill open">OPEN</span><span class="pnl">+$90<small>+2.1%</small></span></div>
      <div class="trow" style="top:201px"><span class="sym"><i class="coin" style="background:#5b5f66"></i>OMT</span><span class="px"><i></i>1.023</span><span class="px"><i></i>1.378</span><span class="pill open">OPEN</span><span class="pnl">+$136<small>+1.8%</small></span></div>
      <div class="trow" style="top:256px"><span class="sym"><i class="coin" style="background:#f3ba2f"></i>VEX</span><span class="px"><i></i>1.209</span><span class="px"><i></i>1.326</span><span class="pill close">CLOSE</span><span class="pnl neg">-$206<small>-1.9%</small></span></div>
      <div class="trow" style="top:311px"><span class="sym"><i class="coin" style="background:#2775ca"></i>LDRC</span><span class="px"><i></i>1.271</span><span class="px"><i></i>1.378</span><span class="pill open">OPEN</span><span class="pnl">+$320<small>+1.8%</small></span></div>
    </div>
  </section>
</div>
</body>
</html>
```